Bramwell Business Cards

Logo files are included. Full "Bramwell" logo should be included on the back of the business card. The B symbol should be included on the front with the contact information.

Bramwell, LLC is the company name and we do commercial construction and real estate development consulting services. Look for a fairly simple card design utilizing our logo.

```html
<!DOCTYPE html>
<html lang="en">
<head>
<meta charset="utf-8">
<title>Bramwell Business Cards</title>
<link rel="stylesheet" href="https://fonts.googleapis.com/css2?family=Poppins:wght@400;500;600;700&display=swap">
<style>
  :root {
    --navy: #1b394e;
    --gold: #eab01c;
    --white: #ffffff;
    --backdrop: #c4c4c4;
  }
  * { box-sizing: border-box; margin: 0; padding: 0; }
  html, body {
    width: 1200px; height: 800px; overflow: hidden;
    background: var(--backdrop);
    font-family: "Poppins", sans-serif;
  }
  .sheet {
    width: 1200px; height: 800px;
    display: flex; align-items: center; justify-content: center; gap: 40px;
  }
  .card {
    position: relative;
    width: 540px; height: 310px;
    background: var(--navy);
    overflow: hidden;
  }
  .card__band {
    position: absolute; left: 0; right: 0; bottom: 0;
    height: 12px; background: var(--gold);
  }

  /* Front: contact side */
  .contact {
    position: absolute; left: 38px; top: 62px; width: 250px;
    color: var(--white);
  }
  .contact__name {
    color: var(--gold); font-weight: 700; font-size: 21px;
    letter-spacing: 0.5px; text-transform: uppercase; line-height: 1.1;
  }
  .contact__title { font-size: 14px; font-weight: 500; margin-top: 2px; }
  .contact__rule {
    width: 130px; height: 1px; background: var(--gold);
    margin: 12px 0 10px;
  }
  .contact__list { list-style: none; }
  .contact__item {
    display: flex; align-items: flex-start; gap: 10px;
    font-size: 13.5px; font-weight: 500; line-height: 1.45;
  }
  .contact__icon { width: 13px; height: 13px; margin-top: 4px; flex: none; fill: var(--gold); }
  .front__emblem {
    position: absolute; right: 36px; top: 38px;
    width: 230px; height: 230px; border-radius: 50%;
    background: var(--white);
    display: flex; align-items: center; justify-content: center;
  }
  .front__emblem-name {
    color: var(--navy); font-weight: 600; font-size: 30px; letter-spacing: 1px;
  }

  /* Back: brand side */
  .brand {
    position: absolute; inset: 0 0 12px 0;
    display: flex; flex-direction: column; align-items: center; justify-content: center;
  }
  .brand__dot {
    width: 62px; height: 62px; border-radius: 50%;
    background: var(--gold); margin-bottom: 16px;
  }
  .brand__name {
    color: var(--white); font-weight: 600; font-size: 50px;
    letter-spacing: 2px; line-height: 1;
  }
  .brand__web {
    color: var(--gold); font-weight: 500; font-size: 14px;
    letter-spacing: 4px; margin-top: 22px;
  }
</style>
</head>
<body>
<main class="sheet">
  <section class="card card--front" aria-label="Business card front">
    <div class="contact">
      <p class="contact__name">Dalen Whitford</p>
      <p class="contact__title">Managing Director</p>
      <div class="contact__rule"></div>
      <ul class="contact__list">
        <li class="contact__item">
          <svg class="contact__icon" viewBox="0 0 16 16" aria-hidden="true"><path d="M3.5 1 6 3.5 4.6 5.4c.9 2.2 2.8 4.1 5 5l1.9-1.4L14 11.5 12.3 14C6.5 13.6 2.4 9.5 2 3.7Z"/></svg>
          <span>044-555 010 234</span>
        </li>
        <li class="contact__item">
          <svg class="contact__icon" viewBox="0 0 16 16" aria-hidden="true"><path d="M1 3h14v10H1Zm1.5 1.2L8 8.6l5.5-4.4Z"/></svg>
          <span>hello@bramwellmail.com</span>
        </li>
        <li class="contact__item">
          <svg class="contact__icon" viewBox="0 0 16 16" aria-hidden="true"><path d="M8 1a7 7 0 1 0 0 14A7 7 0 0 0 8 1Zm0 1.4c.7.8 1.3 2 1.5 3.6h-3C6.7 4.4 7.3 3.2 8 2.4ZM2.5 7h2.9c0 .7 0 1.3.1 2H2.5a5.6 5.6 0 0 1 0-2Zm4 0h3a12 12 0 0 1 0 2h-3a12 12 0 0 1 0-2Zm4.1 0h2.9a5.6 5.6 0 0 1 0 2h-2.9c.1-.7.1-1.3 0-2ZM8 13.6c-.7-.8-1.3-2-1.5-3.6h3c-.2 1.6-.8 2.8-1.5 3.6Z"/></svg>
          <span>www.bramwellco.com</span>
        </li>
      </ul>
      <div class="contact__rule"></div>
      <ul class="contact__list">
        <li class="contact__item">
          <svg class="contact__icon" viewBox="0 0 16 16" aria-hidden="true"><path d="M8 1a5 5 0 0 0-5 5c0 3.6 5 9 5 9s5-5.4 5-9a5 5 0 0 0-5-5Zm0 7a2 2 0 1 1 0-4 2 2 0 0 1 0 4Z"/></svg>
          <span>48, Alder Lane<br>Country name, 560210</span>
        </li>
      </ul>
    </div>
    <div class="front__emblem">
      <span class="front__emblem-name">Bramwell</span>
    </div>
    <div class="card__band"></div>
  </section>

  <section class="card card--back" aria-label="Business card back">
    <div class="brand">
      <div class="brand__dot"></div>
      <p class="brand__name">BRAMWELL</p>
      <p class="brand__web">WWW.BRAMWELL.COM</p>
    </div>
    <div class="card__band"></div>
  </section>
</main>
</body>
</html>
```